Brill Insurance Agency - Business Cards

Hello, I am needing new trendy business cards for our Insurance Agency now that I have a new Logo. I have attached our new logo with several color options along with a business card design that I like. I am leaning towards burgundy and blue colors. I have attached our current business card. I have also attached a headshot of our company president, Martin Vale, that you can use if you wish. Thank you so much in advance for all the wonderful designs!!!!

Target Market(s)

We want to look very professional to potential customers and we also want to look very professional so insurance companies will want to contract with us to sell their product.

Industry/Entity Type

Insurance

Contact Information for Business Card

Martin Vale
mvale@brillagency.com
Business: 555-213-4087
Fax: 555-213-7751
Cell: 555-390-2618
Toll Free: 888-555-0194
42 W Elm Rd Butler, MO 64730
www.brillagency.net

Font styles to use
Serif
Sans Serif

Colors
0355a3
3277b5
f04a50
ec1f27

Requirements
Nice to have
• I love creativity. The more creative and balanced a business card design the more I will like it. I would like the card to be printed horizontally instead of vertically.
Should not have
• My project should not have the Allied Coverage Network logo. It is no longer used in the industry.

```html
<!DOCTYPE html>
<html lang="en">
<head>
<meta charset="utf-8">
<title>Brill Insurance Agency – Business Cards</title>
<link href="https://fonts.googleapis.com/css2?family=Montserrat:wght@600;700&family=Lato:wght@400;700&display=swap" rel="stylesheet">
<style>
  :root {
    --backdrop: #2f2f2f;
    --card-light: #ececec;
    --card-grey: #4d4d4d;
    --burgundy: #540f27;
    --ink: #1e1e1e;
    --rule: #8a8a8a;
    --white: #ffffff;
  }
  * { margin: 0; padding: 0; box-sizing: border-box; }
  html, body { width: 1200px; height: 1200px; overflow: hidden; }
  body {
    background: var(--backdrop);
    position: relative;
    font-family: "Lato", Arial, sans-serif;
  }
  .card {
    position: absolute;
    top: 310px;
    width: 366px;
    height: 593px;
    box-shadow: 0 6px 18px rgba(0,0,0,.45);
    overflow: hidden;
  }
  /* Front */
  .card-front {
    left: 233px;
    background: var(--card-light);
    text-align: center;
    color: var(--ink);
  }
  .brand-mark {
    position: absolute;
    left: 50%;
    top: 68px;
    width: 96px;
    height: 96px;
    margin-left: -48px;
    border: 8px solid var(--card-grey);
    border-radius: 50%;
  }
  .brand-name {
    position: absolute;
    top: 198px;
    left: 0; right: 0;
    font-family: "Montserrat", Arial, sans-serif;
    font-weight: 700;
    color: var(--burgundy);
    font-size: 27px;
    letter-spacing: .3px;
    line-height: 1;
  }
  .brand-sub {
    position: absolute;
    top: 230px;
    left: 50px; right: 48px;
    display: flex;
    align-items: center;
    gap: 6px;
    font-family: "Montserrat", Arial, sans-serif;
    font-weight: 600;
    font-size: 15px;
    letter-spacing: 4px;
    color: var(--card-grey);
    line-height: 1;
  }
  .brand-sub::before, .brand-sub::after {
    content: "";
    flex: 1;
    height: 2px;
    background: var(--card-grey);
  }
  .person-name {
    position: absolute;
    top: 314px; left: 0; right: 0;
    font-family: "Montserrat", Arial, sans-serif;
    font-weight: 600;
    font-size: 20px;
    color: var(--burgundy);
  }
  .person-title {
    position: absolute;
    top: 337px; left: 0; right: 0;
    font-size: 17px;
  }
  .icon-row {
    position: absolute;
    top: 366px; left: 58px; right: 58px;
    display: flex;
    align-items: center;
    gap: 5px;
  }
  .icon-row::before, .icon-row::after {
    content: "";
    flex: 1;
    height: 1px;
    background: var(--rule);
  }
  .icon-row::before { margin-right: 2px; }
  .icon-row::after { margin-left: 2px; }
  .icon {
    width: 24px; height: 24px;
    background: var(--burgundy);
    display: flex; align-items: center; justify-content: center;
  }
  .icon svg { width: 16px; height: 16px; }
  .contact-list {
    position: absolute;
    top: 399px; left: 0; right: 0;
    list-style: none;
    font-size: 16.5px;
    line-height: 20.3px;
  }
  .divider {
    position: absolute;
    top: 507px; left: 58px; right: 58px;
    height: 1px;
    background: var(--ink);
  }
  .address {
    position: absolute;
    top: 514px; left: 0; right: 0;
    font-size: 16.5px;
    line-height: 22px;
    font-style: normal;
  }
  /* Back */
  .card-back {
    left: 628px;
    background: var(--card-grey);
  }
  .card-back .band { position: absolute; inset: 0; }
  .tagline {
    position: absolute;
    top: 86px; left: 0; right: 0;
    text-align: center;
    color: var(--white);
    font-size: 19.5px;
    letter-spacing: .2px;
  }
  .back-name {
    position: absolute;
    top: 239px; left: 0; width: 290px;
    text-align: center;
    color: var(--white);
    font-family: "Montserrat", Arial, sans-serif;
    font-weight: 700;
    font-size: 24px;
    line-height: 30px;
  }
  .partner-badge {
    position: absolute;
    left: 108px; top: 507px;
    width: 156px; height: 36px;
  }
</style>
</head>
<body>

<section class="card card-front">
  <div class="brand-mark"></div>
  <div class="brand-name">BRILL INSURANCE</div>
  <div class="brand-sub">AGENCY INC</div>

  <div class="person-name">NOLAN PIERCE</div>
  <div class="person-title">Managing Director</div>

  <div class="icon-row">
    <span class="icon"><svg viewBox="0 0 16 16" fill="#fff"><path d="M2 6c0-2 3-3 6-3s6 1 6 3l-2 1-1-2H5L4 7z"/><rect x="4" y="8" width="8" height="5" rx="1"/></svg></span>
    <span class="icon"><svg viewBox="0 0 16 16" fill="none" stroke="#fff" stroke-width="1.5"><rect x="5" y="2" width="6" height="12" rx="1"/><path d="M7 12h2"/></svg></span>
    <span class="icon"><svg viewBox="0 0 16 16" fill="#fff"><rect x="5" y="2" width="6" height="4"/><rect x="2" y="6" width="12" height="5" rx="1"/><rect x="5" y="10" width="6" height="4" fill="none" stroke="#fff"/></svg></span>
    <span class="icon"><svg viewBox="0 0 16 16" fill="none" stroke="#fff" stroke-width="1.3"><rect x="2" y="4" width="12" height="8"/><path d="M2 4l6 5 6-5"/></svg></span>
    <span class="icon"><svg viewBox="0 0 16 16" fill="none" stroke="#fff" stroke-width="1.3"><circle cx="8" cy="8" r="5.5"/><path d="M2.5 8h11M8 2.5c-2 2-2 9 0 11M8 2.5c2 2 2 9 0 11"/></svg></span>
  </div>

  <ul class="contact-list">
    <li>444 555 6688</li>
    <li>888 555 4433</li>
    <li>888 444 0000</li>
    <li>info@webname.com</li>
    <li>www.websitename.com</li>
  </ul>
  <div class="divider"></div>
  <address class="address">12345, Address Goes Here<br>Country Name, 123456.</address>
</section>

<section class="card card-back">
  <svg class="band" viewBox="0 0 366 593" preserveAspectRatio="none">
    <polygon points="0,498 366,338 366,593 0,593" fill="var(--burgundy)"/>
    <circle cx="145" cy="297" r="135" fill="none" stroke="var(--white)" stroke-width="16"/>
  </svg>
  <div class="tagline">THE RIGHT CHOICE MADE EASY!</div>
  <div class="back-name">BRILL<br>INSURANCE<br>AGENCY</div>
  <svg class="partner-badge" role="img" aria-label="Partner network badge" viewBox="0 0 156 36">
    <rect x="1" y="1" width="154" height="34" rx="17" fill="none" stroke="var(--white)" stroke-width="2"/>
  </svg>
</section>

</body>
</html>
```